Pelkman Agency (http://pa.quorvexstudio.com/)

We are looking for a similar design to what we have, but more professional looking and cleaned up with links and logo that is not so grainy looking. We are an independent insurance agency marketing to personal and commercial clients. We offer all commercial lines markets and all personal lines. We target excavators, landscapers, restaurants, golf courses, contractors. Please look at http://pa.quorvexstudio.com/ which we had designed but do not like it, it will give you an idea of what we are looking for.

Target Market(s)

Commercial and personal insurance. All business products and all personal (homeowners, auto, antique auto, umbrella)

Industry/Entity Type

It Professional

Logo Text

Knowledge Building Your Assurance

Number of Pages Required

5+ page

Colors
000000
848484
0255a3

```html
<!DOCTYPE html>
<html lang="en">
<head>
<meta charset="utf-8">
<title>Pelkman Agency</title>
<link href="https://fonts.googleapis.com/css2?family=Alegreya:ital,wght@0,400;0,700;1,400;1,700&family=Alegreya+Sans:wght@400;500;700;800&display=swap" rel="stylesheet">
<style>
:root{
  --blue:#0255a3;
  --blue-dark:#013f7c;
  --grey:#848484;
  --black:#000000;
  --ink:#1a1a1a;
  --text:#2b2b2b;
  --soft:#f4f4f4;
  --rule:#d8d8d8;
  --white:#ffffff;
}
*{box-sizing:border-box;margin:0;padding:0}
html,body{width:1200px;height:2219px;overflow:hidden;background:var(--white)}
body{position:relative;font-family:'Alegreya',Georgia,serif;color:var(--text)}
.abs{position:absolute}

/* header */
.site-header{position:absolute;left:0;top:0;width:1200px;height:85px;background:var(--white);border-bottom:4px solid var(--blue);z-index:3}
.brand-tab{position:absolute;left:74px;top:0;width:172px;height:106px;background:var(--white);border-radius:0 0 24px 24px;z-index:4;display:flex;flex-direction:column;align-items:center;justify-content:center;gap:8px;box-shadow:0 3px 4px rgba(0,0,0,.12)}
.brand-mark{width:16px;height:16px;background:var(--blue)}
.brand-name{font-family:'Alegreya',Georgia,serif;font-weight:700;font-size:21px;color:var(--ink)}
.phone{position:absolute;right:91px;top:12px;font-family:'Alegreya Sans',sans-serif;font-weight:800;font-size:22px;color:var(--blue);display:flex;align-items:center;gap:6px}
.main-nav{position:absolute;right:91px;top:48px;display:flex;gap:27px;font-family:'Alegreya Sans',sans-serif;font-weight:700;font-size:15px;color:var(--ink);letter-spacing:.2px}

/* hero */
.hero{position:absolute;left:0;top:85px;width:1200px;height:495px;background:linear-gradient(100deg,#c9c6c0 0%,#8f8780 28%,#4b4a4a 48%,#b9a896 62%,#6d7f96 78%,#3c3f44 100%)}
.hero-caption{position:absolute;left:0;bottom:0;width:1200px;height:70px;background:rgba(20,20,20,.78)}
.hero-title{position:absolute;left:91px;top:12px;font-size:42px;color:var(--white);font-weight:400}
.hero-dots{position:absolute;right:91px;top:10px;display:flex;gap:3px}
.hero-dots i{width:8px;height:8px;border-radius:50%;background:#bbb}
.hero-dots i.on{background:var(--blue)}
.hero-cta{position:absolute;right:91px;top:34px;font-weight:700;font-style:italic;font-size:15px;color:var(--white);text-decoration:underline}

/* section headings */
.section-title{position:absolute;left:91px;font-family:'Alegreya Sans',sans-serif;font-weight:800;font-size:29px;letter-spacing:.3px;text-transform:uppercase;width:620px;padding-bottom:5px;border-bottom:2px solid var(--rule)}
.section-title b{color:var(--blue);font-weight:800}
.section-title span{color:var(--grey)}

.btn-more{position:absolute;height:26px;padding:0 17px;border:1px solid #b5b5b5;border-radius:6px;background:linear-gradient(#fafafa,#d9d9d9);font-family:'Alegreya Sans',sans-serif;font-weight:700;font-style:italic;font-size:12px;color:var(--grey);line-height:24px}

/* who we are */
.about-lead{position:absolute;left:91px;top:690px;font-weight:700;font-size:20px;color:var(--ink)}
.about-text{position:absolute;left:91px;top:720px;width:740px;font-size:14.5px;line-height:21.3px;color:var(--text)}
.team-photo{position:absolute;left:846px;top:695px;width:263px;height:193px;background:linear-gradient(180deg,#e9e9e9,#9a9a9a 60%,#4a4f57)}

/* what we provide */
.services{position:absolute;left:0;top:1002px;width:1200px;height:526px;background:var(--soft);border-top:1px solid #e2e2e2;border-bottom:1px solid #e2e2e2}
.service{position:absolute;top:114px;width:228px}
.service-photo{height:134px;border-bottom:4px solid var(--blue)}
.service h3{margin-top:8px;font-weight:700;font-size:19px;color:var(--ink)}
.service p{margin-top:2px;font-size:14px;line-height:19.2px;color:var(--text)}
.service .btn-more{position:static;display:inline-block;margin-top:8px}
.arrow{position:absolute;top:228px}
.slider-dots{position:absolute;left:580px;top:446px;display:flex;gap:3px}
.slider-dots i{width:8px;height:8px;border-radius:50%;background:#c4c4c4}
.slider-dots i.on{background:var(--blue)}

/* testimonials */
.avatar{position:absolute;left:91px;top:1644px;width:140px;height:140px;border-radius:50%;border:4px solid var(--blue);background:radial-gradient(circle at 50% 40%,#d7c2ad,#6b7d94 70%)}
.quote-mark{position:absolute;left:236px;top:1630px;font-size:56px;color:#c8c8c8;font-style:italic;font-weight:700}
.quote{position:absolute;left:268px;top:1656px;width:490px;font-style:italic;font-size:14.3px;line-height:20px;color:var(--text)}
.quote cite{display:block;font-weight:700;font-style:italic;color:var(--ink)}

.contact-card{position:absolute;left:794px;top:1598px;width:315px;height:270px;border:1px solid #c5c5c5;border-radius:6px;background:linear-gradient(#f6f6f6,#d2d2d2)}
.contact-card .section-title{left:12px;top:10px;width:290px;font-size:29px}
.field{position:absolute;left:13px;width:289px;height:34px;background:var(--white);border:1px solid #e1e1e1;font-size:13px;color:var(--grey);padding:8px 10px}
.send{position:absolute;left:13px;top:216px;height:34px;padding:0 17px;border-radius:6px;background:linear-gradient(var(--blue),var(--blue-dark));font-family:'Alegreya Sans',sans-serif;font-weight:800;font-style:italic;font-size:15px;color:var(--white);line-height:34px}

/* footer */
.site-footer{position:absolute;left:0;top:1958px;width:1200px;height:261px;background:var(--black);border-top:4px solid var(--blue)}
.top-tab{position:absolute;left:573px;top:-22px}
.footer-brand{position:absolute;left:90px;top:64px;width:140px;text-align:center}
.footer-brand .brand-mark{margin:0 auto 10px;width:20px;height:20px;background:var(--grey)}
.footer-brand strong{display:block;font-size:21px;color:var(--grey)}
.footer-brand small{font-size:11px;font-style:italic;color:var(--grey)}
.footer-col{position:absolute;top:50px;width:180px}
.footer-col h4{font-family:'Alegreya Sans',sans-serif;font-weight:800;font-size:14px;color:var(--grey);padding-bottom:6px;border-bottom:1px solid #333;margin-bottom:8px}
.footer-col li{list-style:none;font-size:13px;line-height:19.3px;color:var(--grey)}
.footer-col li::before{content:"> ";}
.footer-col p{font-size:13px;line-height:17px;color:var(--grey)}
.socials{display:flex;gap:4px;margin-top:10px}
.socials i{width:20px;height:20px;border-radius:50%;background:var(--grey)}
</style>
</head>
<body>

<header class="site-header">
  <div class="phone">
    <svg width="16" height="16" viewBox="0 0 24 24" aria-hidden="true"><path fill="#0255a3" d="M6.6 10.8a15.1 15.1 0 0 0 6.6 6.6l2.2-2.2a1 1 0 0 1 1-.25 11.4 11.4 0 0 0 3.6.57 1 1 0 0 1 1 1V20a1 1 0 0 1-1 1A17 17 0 0 1 3 4a1 1 0 0 1 1-1h3.5a1 1 0 0 1 1 1c0 1.25.2 2.45.57 3.57a1 1 0 0 1-.25 1z"/></svg>
    1.888.4.PELKMAN
  </div>
  <nav class="main-nav">
    <span>PERSONAL</span><span>BUSINESS</span><span>SERVICE CENTER</span><span>TESTIMONIALS</span><span>ABOUT US</span><span>CONTACT US</span>
  </nav>
</header>
<div class="brand-tab">
  <div class="brand-mark"></div>
  <div class="brand-name">Pelkman Agency</div>
</div>

<section class="hero" role="img" aria-label="Smiling woman sitting in the driver's seat of a car holding out keys">
  <div class="hero-caption">
    <h1 class="hero-title">Auto Insurance</h1>
    <div class="hero-dots"><i class="on"></i><i></i><i></i><i></i><i></i></div>
    <div class="hero-cta">Get a Quote »</div>
  </div>
</section>

<h2 class="section-title" style="top:640px"><b>Who</b> <span>we are</span></h2>
<div class="about-lead">Small Enough to Care, Big Enough To Make a Difference</div>
<p class="about-text">Lorem ipsum dolor sit amet, consectetur adipiscing elit. Cras sodales sapien sed lacus bibendum scelerisque. Nulla et sem auctor, tempus quam quis, accumsan mi. Aliquam quis dictum purus. Integer id aliquam libero. Fusce odio nulla, viverra at bibendum vel, euismod nec velit. In lacinia consequat venenatis. Nullam finibus sollicitudin ultricies. Aenean quis dictum diam, ut tempor justo. Pellentesque habitant morbi tristique senectus et netus et malesuada fames ac turpis egestas. Etiam vel nunc nunc. Vestibulum bibendum ex a dui ultrices, sit amet rhoncus est accumsan. Vestibulum id bibendum sem. Aliquam eros augue, luctus eget bibendum id, luctus eget neque. Nunc cup rsusy interdum elit. Phasellus vehicula tellus ac viverra interdum. Sed sapien lectus, molestie sit amet pretium ut, ornare vitae ligula. Pellentesque ornare pretium leo. Nullam in augue eu neque hendrerit imperdiet non vitae.</p>
<div class="team-photo" role="img" aria-label="Team of business people in suits standing together"></div>
<div class="btn-more" style="left:91px;top:904px">Learn More »</div>

<section class="services">
  <h2 class="section-title" style="top:60px"><b>What</b> <span>we provide</span></h2>
  <svg class="arrow" style="left:54px" width="20" height="50" viewBox="0 0 20 50" aria-hidden="true"><path d="M17 2 3 25l14 23" fill="none" stroke="#9a9a9a" stroke-width="2"/></svg>
  <svg class="arrow" style="left:1126px" width="20" height="50" viewBox="0 0 20 50" aria-hidden="true"><path d="M3 2l14 23L3 48" fill="none" stroke="#9a9a9a" stroke-width="2"/></svg>

  <article class="service" style="left:91px">
    <div class="service-photo" role="img" aria-label="Smiling senior couple" style="background:linear-gradient(135deg,#e8d2bd,#b88f74 50%,#f2f2f2)"></div>
    <h3>Personal Insurance</h3>
    <p>Pellentesque vel orci non turpis tincidunt iaculis. Nullam facilisis ultrices dui, id vestibulum lorem eleifend vel. Donec auctor dolor odio, eget venenatis felis laoreet.</p>
    <div class="btn-more">Learn More »</div>
  </article>
  <article class="service" style="left:354px">
    <div class="service-photo" role="img" aria-label="Mechanic working under a car in a garage" style="background:linear-gradient(135deg,#d9d9d9,#6d6d6d 55%,#2f4e7e)"></div>
    <h3>Business Insurance</h3>
    <p>Sed sapien lectus, molestie sit amet pretium ut, ornare vitae ligula. Pell ornare pretium leo. Nullam in aug ueeu neque hendrerit imperdiet non vitae. mauris eu vestibulum.</p>
    <div class="btn-more">Learn More »</div>
  </article>
  <article class="service" style="left:618px">
    <div class="service-photo" role="img" aria-label="Young family sitting in the open back of a car" style="background:linear-gradient(135deg,#8a8a8a,#ece8e2 50%,#b37f63)"></div>
    <h3>Auto Insurance</h3>
    <p>Integer tristique, nisi et consequat euismod, ex lorem finibus sem, sed bibendum magna urna a dolor. Etiam pretium non eros eu elemen tum mam quam dolor celerisque.</p>
    <div class="btn-more">Learn More »</div>
  </article>
  <article class="service" style="left:881px">
    <div class="service-photo" role="img" aria-label="Large lit house at dusk" style="background:linear-gradient(180deg,#3d5f9a,#6f6a66 55%,#d49a4c)"></div>
    <h3>Property Insurance</h3>
    <p>Vivamus ut rutrum nisi. Morbi sed tellus congue, lacinia libero eget, iaculis nulla. Curabitur urna enim, convallis eu vestibulum ut, interd um nec tortor vulputate leoa variu.</p>
    <div class="btn-more">Learn More »</div>
  </article>
  <div class="slider-dots"><i class="on"></i><i></i><i></i><i></i></div>
</section>

<h2 class="section-title" style="top:1590px"><b>What</b> <span>our clients say</span></h2>
<div class="avatar" role="img" aria-label="Portrait of a smiling client in a suit"></div>
<div class="quote-mark">“</div>
<blockquote class="quote">Donec at neque quis arcu pulvinar posuere. Nullam lobortis ligula faucibus tortor varius finibus. Proin ut nisi finibus ex euismod aliquet ac a elit. Quisque sed tincidunt massa. Phasellus luctus mauris ut diam aliquam, at sagittis ex interdum. In blandit odio ut sem auctor, vitae ultricies orci imperdiet. Curabitur at nisl ultricies quam venenatis ullamcorper et ac enim. Mauris bibendum imperdiet ex commodo...
  <cite>— Marcus Hale, Hale Supply</cite>
</blockquote>
<div class="btn-more" style="left:91px;top:1802px">View All Testimonials »</div>

<form class="contact-card">
  <h2 class="section-title"><b>Contact</b> <span>us</span></h2>
  <div class="field" style="top:58px">Name</div>
  <div class="field" style="top:97px">Email</div>
  <div class="field" style="top:136px;height:70px">Message</div>
  <div class="send">SEND A MESSAGE »</div>
</form>

<footer class="site-footer">
  <svg class="top-tab" width="54" height="24" viewBox="0 0 54 24" aria-hidden="true"><path d="M0 24 16 0h22l16 24z" fill="#000"/><path d="M27 6v13M21 12l6-6 6 6" fill="none" stroke="#848484" stroke-width="3"/></svg>
  <div class="footer-brand">
    <div class="brand-mark"></div>
    <strong>Pelkman Agency</strong>
    <small>©2015 Pelkman Agency.</small>
  </div>
  <div class="footer-col" style="left:302px">
    <h4>PELKMAN AGENCY</h4>
    <ul><li>Home</li><li>Personal</li><li>Business</li><li>Service Center</li><li>Testimonials</li><li>About Us</li><li>Contact Us</li><li>Private Policy</li></ul>
  </div>
  <div class="footer-col" style="left:513px">
    <h4>PERSONAL INSURANCE</h4>
    <ul><li>Annuity Insurance</li><li>Auto Insurance</li><li>Property Insurance</li><li>Life Insurance</li><li>Long Term Care Insurance</li></ul>
  </div>
  <div class="footer-col" style="left:724px">
    <h4>BUSINESS INSURANCE</h4>
    <ul><li>Carpenters Insurance</li><li>Electricians Insurance</li><li>Excavators Insurance</li><li>Golf Courses Insurance</li><li>Landscapers Insurance</li><li>Plumbing Insurance</li><li>Restaurants Insurance</li><li>Trucking Insurance</li></ul>
  </div>
  <div class="footer-col" style="left:934px">
    <h4>CONTACT US</h4>
    <p>P: 1.888.4.PELKMAN<br>E: <u>admin@pelkmanagency.com</u></p>
    <p style="margin-top:16px">Office Hours:<br>Mon. thru Fri. 7 am to 5pm</p>
    <div class="socials"><i></i><i></i><i></i></div>
  </div>
</footer>

</body>
</html>
```